New Webpage for High Class Expert Witness Services Company

We are looking for a minimalist design for a webpage that just has our logo and an entry form offer to connect with one of our Liaisons.
The entry form should just ask for Name, Email, Contact Info and Description of Project.

Company Name is: The Marlowe Crest Defense Services

Number of Pages Required

1 page

```html
<!DOCTYPE html>
<html lang="en">
<head>
<meta charset="utf-8">
<title>The Marlowe Crest Defense Services</title>
<link rel="stylesheet" href="https://fonts.googleapis.com/css2?family=Lato:wght@400;700&family=Noto+Serif:wght@400;700&family=Cousine&display=swap">
<style>
  :root {
    --ink: #000000;
    --header: #121212;
    --panel: #c2c3c6;
    --field: #ffffff;
    --field-text: #555a60;
    --icon: #6b7077;
    --white: #ffffff;
    --logo-box: #1b1b1b;
    --rule: #3a3a3a;
    --hero-a: #2c3446;
    --hero-b: #4a4f66;
    --hero-c: #1a1d2a;
  }
  * { box-sizing: border-box; margin: 0; padding: 0; }
  html, body { width: 821px; height: 1200px; overflow: hidden; background: var(--ink); }
  body { position: relative; font-family: "Lato", sans-serif; color: var(--white); }

  .site-header { position: absolute; left: 0; top: 0; width: 821px; height: 59px; background: var(--header); display: flex; align-items: center; justify-content: center; }
  .brand { display: flex; align-items: center; gap: 8px; }
  .brand-mark { width: 14px; height: 14px; border: 1.5px solid var(--white); }
  .brand-name { font-family: "Noto Serif", serif; font-weight: 400; color: var(--white); letter-spacing: 1.5px; font-size: 14px; text-transform: uppercase; }

  .hero { position: absolute; left: 0; top: 59px; width: 821px; height: 409px;
    background: linear-gradient(100deg, var(--hero-b) 0%, var(--hero-a) 35%, var(--hero-c) 70%, #3a3f6a 100%); }
  .hero-title { position: absolute; left: 0; right: 0; top: 72px; text-align: center; font-family: "Noto Serif", serif; font-weight: 700; font-size: 39px; line-height: 50px; letter-spacing: 0.3px; text-shadow: 0 2px 6px rgba(0,0,0,.5); }
  .hero-sub { position: absolute; left: 0; right: 0; top: 179px; text-align: center; font-weight: 700; font-size: 14px; text-shadow: 0 1px 4px rgba(0,0,0,.6); }

  .consult { position: absolute; left: 76px; top: 373px; width: 670px; height: 242px; background: var(--panel); border-radius: 10px; }
  .consult h2 { position: absolute; left: 0; right: 0; top: 24px; text-align: center; font-family: "Noto Serif", serif; font-weight: 700; font-size: 26px; color: var(--ink); }
  .field { position: absolute; width: 293px; height: 32px; background: var(--field); border-radius: 4px; box-shadow: 0 1px 3px rgba(0,0,0,.2); display: flex; align-items: center; padding-left: 15px; gap: 9px; font-size: 11px; color: var(--field-text); }
  .field svg { width: 12px; height: 12px; fill: var(--icon); flex: none; }
  .field .chev { position: absolute; right: 14px; width: 10px; height: 10px; fill: none; stroke: #333; stroke-width: 1.5; }
  .f-name { left: 28px; top: 80px; }
  .f-email { left: 28px; top: 124px; }
  .f-desc { left: 349px; top: 80px; }
  .f-phone { left: 349px; top: 123px; }
  .submit { position: absolute; left: 287px; top: 184px; width: 111px; height: 32px; background: #111; color: var(--white); border-radius: 3px; font-weight: 700; font-size: 12px; display: flex; align-items: center; justify-content: center; }

  .about-frame-a { position: absolute; left: 75px; top: 683px; width: 185px; height: 160px; border: 1.5px solid var(--white); border-right: none; border-bottom: none; border-radius: 6px 6px 0 6px; }
  .about-frame-a::after { content: ""; position: absolute; right: 0; top: -1.5px; width: 0; }
  .about-frame-b { position: absolute; left: 210px; top: 800px; width: 185px; height: 160px; border: 1.5px solid var(--white); border-left: none; border-top: none; border-radius: 0 6px 6px 6px; }
  .about-image { position: absolute; left: 82px; top: 690px; width: 305px; height: 264px; border-radius: 6px;
    background: radial-gradient(circle at 50% 48%, #6e8fb4 0%, #34506f 35%, #16253a 75%, #0c1523 100%); }

  .about { position: absolute; left: 441px; top: 676px; width: 304px; }
  .about h2 { font-family: "Noto Serif", serif; font-weight: 700; font-size: 26px; margin-bottom: 14px; }
  .about p { font-size: 10.5px; line-height: 17.6px; text-align: justify; }
  .about p.note { font-family: "Cousine", monospace; font-size: 9.4px; margin-top: 6px; }

  .site-footer { position: absolute; left: 0; top: 1004px; width: 821px; text-align: center; }
  .footer-brand { margin: 0 auto; width: 275px; height: 71px; background: var(--logo-box); display: flex; align-items: center; justify-content: center; gap: 9px; }
  .footer-brand .brand-name { font-size: 15px; }
  .tagline { margin-top: 14px; font-size: 10.5px; }
  .contacts { margin-top: 16px; display: flex; justify-content: center; gap: 46px; font-size: 10.5px; }
  .contacts span { display: flex; align-items: center; gap: 10px; }
  .contacts svg { width: 11px; height: 11px; fill: var(--white); }
  .rule { position: absolute; left: 77px; top: 1159px; width: 668px; height: 1px; background: var(--rule); }
  .copyright { position: absolute; left: 0; right: 0; top: 1168px; text-align: center; font-size: 10.5px; }
</style>
</head>
<body>
  <header class="site-header">
    <div class="brand"><span class="brand-mark"></span><span class="brand-name">Marlowe Crest Defense Services</span></div>
  </header>

  <section class="hero" role="img" aria-label="Photo of a modern executive office at night with floor-to-ceiling windows overlooking city skyscrapers">
    <h1 class="hero-title">DEFENSE EXPERTISE<br>WHEN IT MATTERS MOST</h1>
    <p class="hero-sub">Connect with seasoned professionals for complex legal matters.</p>
  </section>

  <form class="consult">
    <h2>Request a Confidential Consultation</h2>
    <div class="field f-name"><svg viewBox="0 0 12 12"><circle cx="6" cy="3.3" r="2.8"/><path d="M0.5 12c0-3.4 2.4-5.2 5.5-5.2s5.5 1.8 5.5 5.2z"/></svg>Name</div>
    <div class="field f-email"><svg viewBox="0 0 12 12"><path d="M0 2h12v8H0z" fill="none" stroke="#6b7077" stroke-width="1.2"/><path d="M0 2l6 4.5L12 2" fill="none" stroke="#6b7077" stroke-width="1.2"/></svg>Email</div>
    <div class="field f-desc"><svg viewBox="0 0 12 12"><path d="M1 1h10v10H1z" fill="none" stroke="#6b7077" stroke-width="1.2"/><rect x="3" y="6" width="1.6" height="3.5"/><rect x="5.3" y="4" width="1.6" height="5.5"/><rect x="7.6" y="5" width="1.6" height="4.5"/></svg>Description of Project<svg class="chev" viewBox="0 0 10 10"><path d="M1 3l4 4 4-4"/></svg></div>
    <div class="field f-phone"><svg viewBox="0 0 12 12"><path d="M2.4 0.5l2 2.3-1.2 1.5c.7 1.6 2 2.9 3.6 3.6l1.5-1.2 2.3 2-1.3 2.1C5 10.6 1.4 7 .4 1.8z"/></svg>Phone Number</div>
    <div class="submit">Submit Inquiry</div>
  </form>

  <div class="about-frame-a"></div>
  <div class="about-frame-b"></div>
  <div class="about-image" role="img" aria-label="Illustration of a glowing shield with a medical cross surrounded by floating virus particles on a dark blue background"></div>

  <section class="about">
    <h2>About Us</h2>
    <p>The Marlowe Crest Defense Services is a trusted provider of elite expert witness support and strategic consulting for attorneys, law firms, corporations, and organizations facing complex legal matters. We specialize in connecting clients with highly qualified professionals whose experience, credibility, and industry knowledge help strengthen cases, clarify technical issues, and support successful outcomes.</p>
    <p class="note">Our team understands that every matter requires discretion, urgency, and precision. That is why we offer a streamlined, confidential process designed to connect you quickly with the right expert resources for your specific</p>
  </section>

  <footer class="site-footer">
    <div class="footer-brand"><span class="brand-mark"></span><span class="brand-name">Marlowe Crest</span></div>
    <p class="tagline">Trusted expert witness services and strategic defense consulting for complex legal matters.</p>
    <div class="contacts">
      <span><svg viewBox="0 0 12 12"><path d="M2.4 0.5l2 2.3-1.2 1.5c.7 1.6 2 2.9 3.6 3.6l1.5-1.2 2.3 2-1.3 2.1C5 10.6 1.4 7 .4 1.8z"/></svg>+1 800 555 0142</span>
      <span><svg viewBox="0 0 12 12"><path d="M0 2h12v8H0z" fill="none" stroke="#fff" stroke-width="1.2"/><path d="M0 2l6 4.5L12 2" fill="none" stroke="#fff" stroke-width="1.2"/></svg>info@marlowecrestdefense.com</span>
    </div>
  </footer>
  <div class="rule"></div>
  <p class="copyright">© 2026 The Marlowe Crest Defense Services. All Rights Reserved.</p>
</body>
</html>
```